Solace Chiropractic & Acupuncture Business Cards

I need a business card design that feels elevated. I am open to any of the logo designs uploaded. We have two doctors so I'll need to be able to change out the names.

Information:
Marnie Toller D.C., Dipl. Ac. ASA
584 W 12th St, Ste 320
Hutchinson, KS 67419
solacegrove.net
620-555-0147
drmarnie@solacegrove.com
Updates

We have designs we like now, we are just trying to choose between top contenders. Thanks for your submissions!

Contact Information for Business Card

noted in description

Requirements
Must have
• ability to edit info if possible
Nice to have
• Please see our website solacegrove.net for our style and colors

```html
<!DOCTYPE html>
<html lang="en">
<head>
<meta charset="utf-8">
<title>Solace Chiropractic &amp; Acupuncture – Business Cards</title>
<link rel="stylesheet" href="https://fonts.googleapis.com/css2?family=Cormorant+Garamond:wght@600&family=Libre+Caslon+Text:wght@400&family=Poppins:wght@400&display=swap">
<style>
  :root {
    --backdrop: #1e1e20;
    --paper: #ffffff;
    --navy: #2f3a52;
    --navy-card: #353d55;
    --navy-deep: #262d40;
    --ink: #2b3246;
  }
  * { margin: 0; padding: 0; box-sizing: border-box; }
  html, body { width: 1200px; height: 1200px; overflow: hidden; }
  body {
    background: var(--backdrop);
    position: relative;
    font-family: "Poppins", sans-serif;
  }
  .card {
    position: absolute;
    top: 204px;
    width: 394px;
    height: 783px;
    border-radius: 26px;
    overflow: hidden;
  }
  .card--front { left: 140px; background: var(--paper); color: var(--ink); }
  .card--back  { left: 634px; background: var(--navy-card); }

  .brand {
    position: absolute;
    top: 110px;
    left: 0; right: 0;
    text-align: center;
    color: var(--navy);
    font-family: "Cormorant Garamond", serif;
    font-weight: 600;
  }
  .brand__dot {
    display: block;
    width: 20px; height: 20px;
    margin: 0 auto 26px;
    border-radius: 50%;
    background: var(--navy);
  }
  .brand__name {
    display: block;
    font-size: 70px;
    letter-spacing: 8px;
    line-height: 1;
    margin-bottom: 26px;
  }
  .brand__tagline {
    display: block;
    font-size: 25px;
    letter-spacing: 1px;
    line-height: 1.15;
  }

  .contact { position: absolute; left: 60px; top: 522px; }
  .contact__name {
    font-family: "Libre Caslon Text", serif;
    font-weight: 400;
    font-size: 24px;
    letter-spacing: 1.5px;
    color: var(--navy);
    line-height: 1.2;
  }
  .contact__creds { font-size: 14px; margin-top: 4px; }
  .contact__address { font-size: 15.5px; line-height: 24px; margin-top: 20px; }
  .contact__list { list-style: none; margin-top: 22px; font-size: 15.5px; }
  .contact__list li { display: flex; align-items: center; gap: 12px; height: 24px; }
  .contact__list svg { width: 13px; height: 13px; fill: var(--ink); flex: none; }

  .back-name {
    position: absolute;
    left: 0; right: 0;
    top: 50%;
    transform: translateY(-50%);
    text-align: center;
    color: var(--navy-deep);
    font-family: "Cormorant Garamond", serif;
    font-weight: 600;
    font-size: 56px;
    letter-spacing: 7px;
    line-height: 1;
  }
</style>
</head>
<body>
  <section class="card card--front">
    <div class="brand">
      <span class="brand__dot"></span>
      <span class="brand__name">SOLACE</span>
      <span class="brand__tagline">CHIROPRACTIC<br>&amp; ACUPUNCTURE</span>
    </div>
    <div class="contact">
      <h1 class="contact__name">MARNIE TOLLER</h1>
      <p class="contact__creds">D.C., Dipl. Ac. ASA</p>
      <p class="contact__address">584 W 12th St, Ste 320<br>Hutchinson, KS 67419</p>
      <ul class="contact__list">
        <li><svg viewBox="0 0 24 24"><path d="M6.6 10.8a15.1 15.1 0 0 0 6.6 6.6l2.2-2.2c.3-.3.7-.4 1-.2 1.1.4 2.3.6 3.6.6.6 0 1 .4 1 1V20c0 .6-.4 1-1 1A17 17 0 0 1 3 4c0-.6.4-1 1-1h3.5c.6 0 1 .4 1 1 0 1.3.2 2.5.6 3.6.1.3 0 .7-.2 1z"/></svg>620-555-0147</li>
        <li><svg viewBox="0 0 24 24"><path d="M2 5h20L12 12.5z M2 7.5l10 7.5 10-7.5V19H2z"/></svg>drmarnie@solacegrove.com</li>
        <li><svg viewBox="0 0 24 24"><circle cx="12" cy="12" r="10"/></svg>www.solacegrove.net</li>
      </ul>
    </div>
  </section>

  <section class="card card--back">
    <p class="back-name">SOLACE</p>
  </section>
</body>
</html>
```